Insurance Company Website Design

We are working with an insurance company. They sell home, auto, commercial, and health insurance. We like the "get a quote" in the banner of https://www.plovanta.example and https://www.quirelmog.example.

Some sites to use for content/competitors and inspiration:
https://velturbrookins.example
https://kamzubredainsurance.example
https://tvorpinsurance.example
https://www.insuranceforzelmarids.example
https://www.plovanta.example
https://www.quirelmog.example

Thank you for taking the time to consider designing a website for us. We are web developers based in Stockton, CA, USA. Most of our projects go through the same process. Understanding this process may help you win a project with us. We custom-code all of our websites in-house. We don’t have any requirements as to what tools you use for your design, but we ask that you follow these guidelines.

IMAGES:
If you use any images or icons in the design, we ask that you have a link to the asset so we can purchase the image/icon. Most of the designs we submit do not have the customer’s images on them unless they have some great images. Be creative; show us the feeling you are trying to portray with your image choices. Use any royalty-free site you choose. We subscribe to Quintrel and mainly use their images, but we can purchase images outside of Quintrel. PLEASE NOTE: we will not submit designs to clients with watermarks on the images.

FONTS:
We ask that you identify the fonts you’re using in the design. This can be done in a message if you want. We typically use Google Fonts and Quintrel Fonts.

CONTENT:
We're always open to different content and ideas. We often submit designs with stock images so the client can see our vision. We typically take pictures after the website launch to use their images with our vision. Lorem Ipsum is fine for paragraphs, but we ask that you make the Headers with correct English. We want to be able to show the vision and identify the sections of the website.

INSPIRATION:
We typically add a couple of links in the brief of websites we like to help you get started in your design.

REVISIONS:
We do not often ask for revisions of the designs unless we see something in the design that may not appeal to the client. If there are slight changes that we want to make, we do that in the development process.

FEEDBACK:
We rarely give feedback on designs during the design process. We are working on many website projects and do not have the time to provide feedback. We usually respond if your request is well thought out and asks specific questions, but a note asking “feedback, please” usually goes unanswered.

```html
<!DOCTYPE html>
<html lang="en">
<head>
<meta charset="utf-8">
<title>Larkhaven Insurance</title>
<link href="https://fonts.googleapis.com/css2?family=Ubuntu:wght@400;500;700&family=Source+Sans+3:ital,wght@0,400;0,600;0,700;1,400&display=swap" rel="stylesheet">
<style>
:root{
  --sky:#5bc5f2;
  --navy:#0f5fad;
  --ink:#1f1f1f;
  --text:#333;
  --muted:#555;
  --topbar:#e6e6e6;
  --footer:#222222;
  --star:#f5a623;
  --white:#fff;
}
*{box-sizing:border-box;margin:0;padding:0}
html,body{width:1200px;height:3293px;overflow:hidden}
body{font-family:"Source Sans 3",sans-serif;color:var(--text);background:var(--white);position:relative}
.abs{position:absolute}
h1,h2,h3{font-family:"Ubuntu",sans-serif;font-weight:500;color:var(--ink)}

/* top bar */
.topbar{left:0;top:0;width:1200px;height:24px;background:var(--topbar);overflow:hidden}
.topbar .band{position:absolute;left:590px;top:0;width:640px;height:24px;background:var(--sky);transform:skewX(-40deg);transform-origin:bottom left}
.topbar .links{position:absolute;right:110px;top:3px;display:flex;gap:28px;font-size:13px;color:#1b2b3a}
/* nav */
.nav{left:0;top:24px;width:1200px;height:73px;border-bottom:1px solid #eee}
.brand{left:111px;top:22px;font-family:"Source Sans 3",sans-serif;font-size:24px;color:var(--navy);font-weight:600;display:flex;align-items:center;gap:8px}
.brand .dot{width:12px;height:12px;border-radius:50%;background:var(--sky)}
.menu{left:370px;top:28px;display:flex;gap:22px;font-size:15px;color:#222}
.login{left:996px;top:18px;width:92px;height:38px;border-radius:10px;background:var(--navy);color:#fff;font-weight:700;font-size:14px;display:flex;align-items:center;justify-content:center}

/* hero */
.hero{left:0;top:97px;width:1200px;height:514px;background:linear-gradient(90deg,#8d7b68 0%,#b7aea2 28%,#c9cdd0 48%,#d7dee4 70%,#dbe3ea 100%)}
.hero .welcome{left:620px;top:90px;width:500px;text-align:center;font-family:"Ubuntu",sans-serif;font-size:26px;color:#222}
.hero h1{left:620px;top:122px;width:500px;text-align:center;font-size:46px}
.quote-card{left:650px;top:203px;width:438px;height:202px;background:#fff;border-radius:6px;box-shadow:0 4px 16px rgba(0,0,0,.08)}
.quote-card p{position:absolute;top:26px;width:100%;text-align:center;font-size:16px;font-weight:600;color:#333}
.field{position:absolute;height:42px;border:1px solid #c9c9c9;border-radius:21px;font-size:16px;color:#999;padding:0 24px;display:flex;align-items:center}
.btn{background:var(--sky);color:#fff;font-weight:700;font-size:14px;border-radius:21px;display:flex;align-items:center;justify-content:center}

/* products */
.sec-title{width:1200px;text-align:center;font-size:40px;line-height:44px}
.product{top:818px;width:292px;height:374px;color:#fff;text-align:center}
.product.light{background:var(--sky)}
.product.dark{background:var(--navy)}
.product .icon{display:block;margin:38px auto 0}
.product h3{color:#fff;font-size:22px;margin-top:10px}
.product p{font-size:15px;line-height:28px;padding:8px 30px 0;color:#eef7ff}
.product .more{margin-top:14px;font-weight:700;font-size:14px;display:flex;justify-content:center;align-items:center;gap:8px}

/* about */
.about h2{left:111px;top:1346px;font-size:40px}
.about .copy{left:111px;top:1418px;width:445px;font-size:16px;line-height:28px;color:#222}
.about .copy p+p{margin-top:9px}
.about-photo{left:607px;top:1291px;width:593px;height:479px;background:linear-gradient(135deg,#cfc7b8,#8b7a66 45%,#5a5048 75%,#c8c0b4)}

/* testimonials */
.t-card{top:1962px;width:315px;height:306px;border:1px solid #eee;box-shadow:0 2px 6px rgba(0,0,0,.05);text-align:center;background:#fff}
.t-card .q{margin:26px auto 0;width:50px;height:50px;border-radius:50%;background:#1f7fd6;color:#fff;font-family:Georgia,serif;font-size:52px;line-height:72px;font-weight:700}
.t-card blockquote{font-style:italic;font-size:14px;line-height:25px;color:#444;padding:18px 24px 0}
.t-card .name{font-weight:600;font-size:15px;color:#222;margin-top:10px}
.t-card .stars{color:var(--star);font-size:11px;letter-spacing:2px}
.chev{stroke:#555;stroke-width:2.5;fill:none}

/* blog */
.b-img{top:2432px;width:315px;height:290px}
.b-card{top:2596px;width:294px;height:254px;background:#fff;box-shadow:0 4px 14px rgba(0,0,0,.09);padding:22px 27px}
.b-card .date{color:var(--sky);font-size:14px}
.b-card h4{font-size:15px;font-weight:600;line-height:25px;color:#222;margin-top:12px}
.b-card p{font-size:15px;line-height:25px;color:#555;margin-top:10px}
.b-card .read{position:absolute;left:27px;bottom:22px;font-size:13px;font-weight:600;color:#444;text-decoration:underline}
.b-card .share{position:absolute;right:30px;bottom:20px}

/* footer */
.footer{left:0;top:2955px;width:1200px;height:338px;background:var(--footer);color:#eee}
.footer .brand-big{left:111px;top:92px;width:210px;text-align:center;font-family:"Source Sans 3",sans-serif;font-size:40px;font-weight:600;color:var(--sky)}
.social{left:164px;top:196px;display:flex;gap:8px}
.social span{width:28px;height:28px;border-radius:50%;background:#fff}
.fcol h5{font-size:15px;font-weight:700;letter-spacing:.3px;color:#fff;margin-bottom:16px}
.fcol li{list-style:none;font-size:14px;line-height:26px}
.contact-row{display:flex;gap:18px;font-size:14px;line-height:26px;margin-bottom:10px}
.copyright{left:0;top:287px;width:1200px;text-align:center;font-size:15px}
</style>
</head>
<body>

<div class="abs topbar"><div class="band"></div>
  <div class="links"><span>Search</span><span>Help</span><span>EN ⌄</span></div>
</div>

<header class="abs nav">
  <div class="abs brand"><span class="dot"></span>Larkhaven</div>
  <nav class="abs menu"><span>Insurance</span><span>Banking</span><span>Investments</span><span>Claims</span><span>Get a Quote</span><span>Pay a Bill</span><span>Find an Agent</span></nav>
  <div class="abs login">LOGIN</div>
</header>

<section class="abs hero">
  <div class="abs" role="img" aria-label="Family sitting under a cardboard roof in their living room" style="left:0;top:0;width:640px;height:514px"></div>
  <div class="abs welcome">Welcome to</div>
  <h1 class="abs">Larkhaven Insurance</h1>
  <div class="abs quote-card">
    <p>Start an insurance quote online.</p>
    <div class="field" style="left:39px;top:67px;width:355px;justify-content:space-between">Product
      <svg width="12" height="8" viewBox="0 0 12 8"><path d="M1 1l5 5 5-5" stroke="#555" stroke-width="1.5" fill="none"/></svg></div>
    <div class="field" style="left:39px;top:119px;width:199px">Zipcode</div>
    <div class="abs btn" style="left:246px;top:119px;width:148px;height:42px">START A QUOTE</div>
  </div>
</section>

<h2 class="abs sec-title" style="top:683px">Our Most Popular<br>Insurance Products</h2>

<div class="abs product light" style="left:0">
  <svg class="icon" width="60" height="60" viewBox="0 0 60 60" fill="none" stroke="#fff" stroke-width="2"><path d="M8 30L28 12l20 18M14 25v22h18"/><circle cx="42" cy="44" r="9"/><path d="M42 38v12M39 41h5a2 2 0 010 4h-4a2 2 0 000 4h5"/></svg>
  <h3>Sell Home</h3>
  <p>Lorem ipsum dolomet, consectetur adipiscing elit, sedeiusmod tempor incididunt ut laboret dolore magna aliqua. Quis ipsum suspendisse ultrices gravida.</p>
  <div class="more">LEARN MORE <svg width="16" height="10" viewBox="0 0 16 10"><path d="M0 5h14M10 1l4 4-4 4" stroke="#fff" stroke-width="1.5" fill="none"/></svg></div>
</div>
<div class="abs product dark" style="left:303px">
  <svg class="icon" width="60" height="60" viewBox="0 0 60 60" fill="none" stroke="#fff" stroke-width="2"><path d="M8 40V30l6-12h22l6 12v10z"/><circle cx="16" cy="34" r="3"/><path d="M8 40v6h6v-6M14 24h24"/><path d="M44 28l10 4v8c0 6-5 10-10 12-5-2-10-6-10-12v-8z" fill="var(--navy)"/><path d="M39 40l4 4 6-7"/></svg>
  <h3>Auto</h3>
  <p>Lorem ipsum dolomet, consectetur adipiscing elit, sedeiusmod tempor incididunt ut laboret dolore magna aliqua. Quis ipsum suspendisse ultrices gravida.</p>
  <div class="more">LEARN MORE <svg width="16" height="10" viewBox="0 0 16 10"><path d="M0 5h14M10 1l4 4-4 4" stroke="#fff" stroke-width="1.5" fill="none"/></svg></div>
</div>
<div class="abs product light" style="left:605px">
  <svg class="icon" width="60" height="60" viewBox="0 0 60 60" fill="none" stroke="#fff" stroke-width="2"><circle cx="30" cy="14" r="7"/><path d="M30 10v8"/><path d="M10 28h40l-4-6H14z"/><path d="M14 34v16h32V34M24 50V40h12v10"/></svg>
  <h3>Commercial</h3>
  <p>Lorem ipsum dolomet, consectetur adipiscing elit, sedeiusmod tempor incididunt ut laboret dolore magna aliqua. Quis ipsum suspendisse ultrices gravida.</p>
  <div class="more">LEARN MORE <svg width="16" height="10" viewBox="0 0 16 10"><path d="M0 5h14M10 1l4 4-4 4" stroke="#fff" stroke-width="1.5" fill="none"/></svg></div>
</div>
<div class="abs product dark" style="left:907px">
  <svg class="icon" width="60" height="60" viewBox="0 0 60 60" fill="none" stroke="#fff" stroke-width="2"><path d="M30 8l18 7v14c0 11-8 18-18 22-10-4-18-11-18-22V15z"/><circle cx="30" cy="30" r="9"/><path d="M30 25v10M25 30h10"/></svg>
  <h3>Health Insurance</h3>
  <p>Lorem ipsum dolomet, consectetur adipiscing elit, sedeiusmod tempor incididunt ut laboret dolore magna aliqua. Quis ipsum suspendisse ultrices gravida.</p>
  <div class="more">LEARN MORE <svg width="16" height="10" viewBox="0 0 16 10"><path d="M0 5h14M10 1l4 4-4 4" stroke="#fff" stroke-width="1.5" fill="none"/></svg></div>
</div>

<section class="about">
  <h2 class="abs">About Us</h2>
  <div class="abs copy">
    <p>Lorem ipsum dolor sit amet, consectetur adipiscing elit, sed do eiusmod tempor incididunt ut labore et dolore magna aliqua. Ut enim ad minim veniam, quis nostrud exercitation ullamco laboris nisi ut aliquip ex ea commodo consequat.</p>
    <p>Duis aute irure dolor in reprehenderit in voluptate velit esse cillum dolore eu fugiat nulla pariatur. Excepteur sint occaecat cupidatat non proident, sunt in culpa qui officia deserunt.</p>
  </div>
  <div class="abs btn" style="left:111px;top:1665px;width:148px;height:41px">START A QUOTE</div>
  <div class="abs about-photo" role="img" aria-label="Young couple reviewing insurance papers with an agent"></div>
</section>

<h2 class="abs sec-title" style="top:1851px">Client Testimonials</h2>
<svg class="abs" style="left:46px;top:2108px" width="16" height="26" viewBox="0 0 16 26"><path class="chev" style="stroke:#aaa" d="M14 2L3 13l11 11"/></svg>
<svg class="abs" style="left:1123px;top:2108px" width="16" height="26" viewBox="0 0 16 26"><path class="chev" d="M2 2l11 11L2 24"/></svg>
<div class="abs t-card" style="left:111px"><div class="q">“</div><blockquote>“ Sed ut perspiciatis unde omnis iste natus error sit voluptat accusantium doloremque laudantium, totam rem aperiam, eaque ipsa quae ab illo inventore veritatis et quasi architect”</blockquote><div class="name">Jhon J.</div><div class="stars">★★★★★</div></div>
<div class="abs t-card" style="left:443px"><div class="q">“</div><blockquote>“ Sed ut perspiciatis unde omnis iste natus error sit voluptat accusantium doloremque laudantium, totam rem aperiam, eaque ipsa quae ab illo inventore veritatis et quasi architect”</blockquote><div class="name">Jhon J.</div><div class="stars">★★★★★</div></div>
<div class="abs t-card" style="left:775px"><div class="q">“</div><blockquote>“ Sed ut perspiciatis unde omnis iste natus error sit voluptat accusantium doloremque laudantium, totam rem aperiam, eaque ipsa quae ab illo inventore veritatis et quasi architect”</blockquote><div class="name">Jhon J.</div><div class="stars">★★★★★</div></div>

<h2 class="abs sec-title" style="top:2340px">Latest Blog</h2>
<svg class="abs" style="left:46px;top:2648px" width="16" height="26" viewBox="0 0 16 26"><path class="chev" style="stroke:#aaa" d="M14 2L3 13l11 11"/></svg>
<svg class="abs" style="left:1123px;top:2648px" width="16" height="26" viewBox="0 0 16 26"><path class="chev" d="M2 2l11 11L2 24"/></svg>
<div class="abs b-img" style="left:111px;background:linear-gradient(160deg,#b9a98a,#8f8a74 40%,#d8d8d8 70%,#6f6a5e)" role="img" aria-label="White car driving on a mountain road"></div>
<div class="abs b-img" style="left:443px;background:linear-gradient(160deg,#e8ece8,#b8c6c9 50%,#4f7fb0)" role="img" aria-label="Agent discussing a clipboard with a senior client"></div>
<div class="abs b-img" style="left:775px;background:linear-gradient(160deg,#d9c3a0,#7b6a58 50%,#2f2b2a)" role="img" aria-label="Two people shaking hands"></div>
<div class="abs b-card" style="left:123px"><div class="date">23 Jan 2024</div><h4>Lorem ipsum dolors, consecte tur adipiscing elit, sed doeiu</h4><p>Lorem ipsum dolor sit amet, ita con sectetur adiisc ing elit, sed do eius mod tempor.</p><span class="read">READ STORY</span><svg class="share" width="20" height="20" viewBox="0 0 20 20" fill="#5bc5f2"><circle cx="15" cy="4" r="3"/><circle cx="5" cy="10" r="3"/><circle cx="15" cy="16" r="3"/><path d="M15 4L5 10l10 6" stroke="#5bc5f2" stroke-width="1.6" fill="none"/></svg></div>
<div class="abs b-card" style="left:455px"><div class="date">23 Jan 2024</div><h4>Lorem ipsum dolors, consecte tur adipiscing elit, sed doeiu</h4><p>Lorem ipsum dolor sit amet, ita con sectetur adiisc ing elit, sed do eius mod tempor.</p><span class="read">READ STORY</span><svg class="share" width="20" height="20" viewBox="0 0 20 20" fill="#5bc5f2"><circle cx="15" cy="4" r="3"/><circle cx="5" cy="10" r="3"/><circle cx="15" cy="16" r="3"/><path d="M15 4L5 10l10 6" stroke="#5bc5f2" stroke-width="1.6" fill="none"/></svg></div>
<div class="abs b-card" style="left:786px"><div class="date">23 Jan 2024</div><h4>Lorem ipsum dolors, consecte tur adipiscing elit, sed doeiu</h4><p>Lorem ipsum dolor sit amet, ita con sectetur adiisc ing elit, sed do eius mod tempor.</p><span class="read">READ STORY</span><svg class="share" width="20" height="20" viewBox="0 0 20 20" fill="#5bc5f2"><circle cx="15" cy="4" r="3"/><circle cx="5" cy="10" r="3"/><circle cx="15" cy="16" r="3"/><path d="M15 4L5 10l10 6" stroke="#5bc5f2" stroke-width="1.6" fill="none"/></svg></div>

<footer class="abs footer">
  <div class="abs brand-big">Larkhaven</div>
  <div class="abs social"><span></span><span></span><span></span></div>
  <div class="abs fcol" style="left:483px;top:70px">
    <h5>CONTACT US</h5>
    <div class="contact-row"><svg width="12" height="16" viewBox="0 0 12 16" style="margin-top:6px"><path d="M6 0a6 6 0 00-6 6c0 4 6 10 6 10s6-6 6-10a6 6 0 00-6-6z" fill="#eee"/><circle cx="6" cy="6" r="2" fill="#222"/></svg><span>Larkhaven Insurance,<br>Address comes here.</span></div>
    <div class="contact-row"><svg width="14" height="14" viewBox="0 0 14 14" style="margin-top:5px"><path d="M3 0l3 3-2 2c1 2 3 4 5 5l2-2 3 3-2 3C6 14 0 8 0 3z" fill="#eee"/></svg><span>+1 555-014-2290</span></div>
    <div class="contact-row"><svg width="14" height="11" viewBox="0 0 14 11" style="margin-top:8px"><rect width="14" height="11" rx="1" fill="#eee"/><path d="M0 1l7 5 7-5" stroke="#222" stroke-width="1.3" fill="none"/></svg><span>hello@larkhavenins.example</span></div>
  </div>
  <div class="abs fcol" style="left:803px;top:70px"><h5>QUICK LINKS</h5><ul><li>Insurance</li><li>Banking</li><li>Investments</li><li>Claims</li><li>Get a Quote</li></ul></div>
  <div class="abs fcol" style="left:993px;top:70px"><h5>OTHER LINKS</h5><ul><li>Pay a Bill</li><li>Find an Agent</li><li>Help</li><li>Contact</li></ul></div>
  <div class="abs copyright">2024 Larkhaven Insurance. All Rights Reserved.</div>
</footer>

</body>
</html>
```